Book Cover for Memoir: Sexual Assault and Traumatic Stress

I need a cover design for a memoir that is a victim's story of a sexual assault. I will need a print-on-demand cover, an eBook cover, and a 3D thumbnail image. The thumbnail and eBook cover will be used immediately, and the POD cover will be used in a few months with the full manuscript is ready. Therefore, I need an artist who is willing to make small adjustments if needed once the page count is set.

I have a image I have purchased that should give you an idea of the desired direction, but you can feel free to use your own images. I have attached some examples of book covers I like. I attached a color palette for fonts.

Overall Look: Fonts should be feminine and thin, but large to stand out. Look should be simple and elegant, and display and overall depressing feeling. There should be enough detail though to make it look professionally put together. Not TOO minimalistic.

I have also attached the Print Harbor templates if you choose to use those. If not, ensure there is an open place for the barcode on the bottom right.

Requirements
Must have
• Title: Beneath Quiet Rain
Subtitle: One Woman's Account of Fear, Guilt & Silence
Author: Dana Ruth Whitford
Audience: Mostly women 18-30
Quote (for the back): "I always thought I'd know how I'd react if I ever was raped. I was wrong. I've been wrong a lot lately."
Summary (back cover): When twenty-seven-year-old Dana Whitford wakes up with a gut-wrenching feeling, she has little memory of the horrifying events that occurred the night before. Days earlier, Dana was a spirited single mom who had abandoned her hometown to raise her daughter in the city and pursue her dreams. In the short months since Dana’s move to Seattle, she became the adored lover of a charismatic lawyer, started a new business, and finally felt life was going her way. So what happened to cause her to break?

In a gripping and heartbreaking narrative, Dana tells the true story of how her life unraveled from the traumatic events that took place that night and why what seems obvious to everyone else is impossible for Dana to believe. Beneath Quiet Rain is a chilling exploration of memory through trauma, trust in humanity, and a captivating story of strength and survival that appeals to the heart of fathers and mothers, sons and daughters, and men and women alike.
Nice to have
• BACK COVER: I'd like to have a photo on the back. This should depict the happy life of the main character before the sexual assault, and should be with her daughter. Or should be a nature scene that starts at the corner and blends into the rest of the cover. I have attached a possible image or you can use something you like.

```html
<!DOCTYPE html>
<html lang="en">
<head>
<meta charset="utf-8">
<title>Beneath Quiet Rain – Print Cover</title>
<link rel="stylesheet" href="https://fonts.googleapis.com/css2?family=Arimo:wght@400;700&family=Tinos:wght@400;700&display=swap">
<style>
  :root {
    --page: #ffffff;
    --wall-light: #eeeeeb;
    --wall-mid: #e2e3df;
    --wall-dark: #b4b6b1;
    --ink: #3f3f3f;
    --ink-soft: #555555;
    --title: #ffffff;
    --title-shadow: rgba(30, 30, 30, 0.6);
    --photo-top: rgba(236, 234, 230, 0);
    --photo-warm: #b89a84;
    --photo-deep: #7a6556;
    --bed-top: rgba(222, 223, 219, 0);
    --bed-mid: #d9d6d0;
    --bed-low: #f1f1ef;
    --box: #ffffff;
    --box-ink: #2a2420;
  }
  * { margin: 0; padding: 0; box-sizing: border-box; }
  html, body {
    width: 1200px; height: 1000px; overflow: hidden;
    background: var(--page);
  }
  .cover-wrap {
    position: absolute; left: 57px; top: 117px;
    width: 1086px; height: 768px;
    background: linear-gradient(90deg, var(--wall-light) 0%, var(--wall-light) 45%, var(--wall-mid) 65%, var(--wall-dark) 100%);
    overflow: hidden;
  }

  /* back cover */
  .back-cover { position: absolute; left: 0; top: 0; width: 498px; height: 768px; }
  .back-photo {
    position: absolute; left: 0; bottom: 0; width: 498px; height: 300px;
    background: linear-gradient(180deg, var(--photo-top) 0%, var(--photo-warm) 45%, var(--photo-deep) 100%);
  }
  .blurb {
    position: absolute; left: 36px; top: 34px; width: 444px;
    font-family: "Arimo", Arial, sans-serif; font-weight: 700;
    font-size: 11.6px; line-height: 15.6px; color: var(--ink-soft);
    text-align: justify;
  }
  .blurb p + p { margin-top: 15px; }
  .back-quote {
    position: absolute; left: 38px; top: 258px; width: 460px;
    font-family: "Tinos", "Times New Roman", serif; font-weight: 700;
    font-size: 17px; line-height: 23px; color: var(--ink-soft);
  }
  .barcode-space {
    position: absolute; left: 321px; top: 635px; width: 167px; height: 103px;
    background: var(--box);
    display: flex; align-items: center; justify-content: center;
    font-family: "Tinos", "Times New Roman", serif; font-weight: 700;
    font-size: 23px; color: var(--box-ink);
  }

  /* spine */
  .spine { position: absolute; left: 498px; top: 0; width: 60px; height: 768px; }
  .spine-title {
    position: absolute; top: 35px; left: 24px;
    writing-mode: vertical-rl;
    font-family: "Tinos", "Times New Roman", serif; font-weight: 700;
    font-size: 28px; line-height: 30px; color: var(--ink-soft);
    white-space: nowrap;
  }
  .spine-subtitle {
    position: absolute; top: 373px; left: 8px;
    writing-mode: vertical-rl;
    font-family: "Tinos", "Times New Roman", serif; font-size: 13px;
    line-height: 14px; color: var(--ink); white-space: nowrap;
  }
  .spine-author {
    position: absolute; top: 572px; left: 20px;
    writing-mode: vertical-rl;
    font-family: "Arimo", Arial, sans-serif; font-weight: 700;
    font-size: 15px; letter-spacing: 0.5px; color: var(--ink);
    white-space: nowrap;
  }

  /* front cover */
  .front-cover { position: absolute; left: 558px; top: 0; width: 528px; height: 768px; }
  .front-photo {
    position: absolute; left: 0; top: 380px; width: 528px; height: 388px;
    background: linear-gradient(180deg, var(--bed-top) 0%, var(--bed-mid) 55%, var(--bed-low) 100%);
  }
  .title {
    position: absolute; left: 52px; top: 22px;
    font-family: "Tinos", "Times New Roman", serif; font-weight: 700;
    font-size: 90px; line-height: 83px; color: var(--title);
    text-shadow: 3px 3px 3px var(--title-shadow);
    white-space: nowrap;
  }
  .subtitle {
    position: absolute; left: 60px; top: 298px;
    font-family: "Tinos", "Times New Roman", serif;
    font-size: 22px; line-height: 25px; color: var(--ink-soft);
  }
  .author {
    position: absolute; left: 61px; top: 474px;
    font-family: "Arimo", Arial, sans-serif; font-weight: 700;
    font-size: 17px; letter-spacing: 0.6px; color: var(--ink);
  }
</style>
</head>
<body>
  <main class="cover-wrap">
    <section class="back-cover">
      <div class="back-photo" role="img" aria-label="Photo of a smiling mother with her baby daughter"></div>
      <div class="blurb">
        <p>When twenty-seven-year-old Dana Whitford wakes up with a gut-wrenching feeling, she has little memory of the horrifying events that occurred the night before. Days earlier, Dana was a spirited single mom who had abandoned her hometown to raise her daughter in the city and pursue her dreams. In the short months since Dana’s move to Seattle, she became the adored lover of a charismatic lawyer, started a new business, and finally felt life was going her way. So what happened to cause her to break?</p>
        <p>In a gripping and heartbreaking narrative, Dana tells the true story of how her life unraveled from the traumatic events that took place that night and why what seems obvious to everyone else is impossible for Dana to believe. Beneath Quiet Rain is a chilling exploration of memory through trauma, trust in humanity, and a captivating story of strength and survival that appeals to the heart of fathers and mothers, sons and daughters, and men and women alike.</p>
      </div>
      <blockquote class="back-quote">"I always thought I'd know how I'd react if I ever was raped.<br>I was wrong. I've been wrong a lot lately."</blockquote>
      <div class="barcode-space">Bar Code</div>
    </section>

    <section class="spine">
      <span class="spine-title">BENEATH QUIET RAIN</span>
      <span class="spine-subtitle">One Woman's Account of Fear,<br>Guilt &amp; Silence</span>
      <span class="spine-author">DANA RUTH WHITFORD</span>
    </section>

    <section class="front-cover">
      <div class="front-photo" role="img" aria-label="Photo of a troubled young woman sitting on a white bed, head resting in her hand"></div>
      <h1 class="title">BENEATH<br>QUIET<br>RAIN</h1>
      <p class="subtitle">One Woman's Account of Fear,<br>Guilt &amp; Silence</p>
      <p class="author">DANA RUTH WHITFORD</p>
    </section>
  </main>
</body>
</html>
```